Kestrel Table Hour Podcast Episode Cover

I’m looking for a clean, professional, and eye-catching podcast episode cover template for my show, Kestrel Table Hour. Each week, I feature a new guest, so the design must allow me (or my team) to easily swap in a new guest’s photo without needing advanced design skills.

The template should be:

- Drag-and-drop friendly: simple for me to replace the guest’s headshot in Canva, Photoshop, or similar.
- On-brand with the Kestrel Table Hour podcast: professional yet approachable, foodservice industry-focused.
- Bold and attention-grabbing for podcast platforms and social media.

Readable text at small sizes, since covers are often viewed as thumbnails.

Design Elements to Include:

1. Podcast Title: “Kestrel Table Hour” (prominently displayed)
2. Subtitle/Space: Line for guest’s name, professional title, and company name
3. Photo Placeholder: Large, central area where I can easily drag and drop a guest photo
4. Brand Colors: attached
5. Clean, modern fonts (easy to read at thumbnail size)
6. Background graphics or patterns that give a sense of foodservice, leadership, or nationwide reach... but do not overpower the guest photo

Format Requirements:

- Editable source file (PSD, Canva template, or layered AI/INDD)
- JPG/PNG exports for immediate use
- Square format (3000x3000px) for podcast platforms

Style Inspiration:
Think modern podcast covers: bold fonts, clean lines, professional with a touch of energy.

Deliverables:

1. Final episode cover template (editable file)
2. Instructions or guidance on how to swap out guest photos

```html
<!DOCTYPE html>
<html lang="en">
<head>
<meta charset="utf-8">
<title>Kestrel Table Hour – Episode Cover</title>
<link href="https://fonts.googleapis.com/css2?family=Anton&family=Oswald:wght@700&family=Allura&family=Poppins:wght@400&display=swap" rel="stylesheet">
<style>
  :root {
    --navy: #1c3a57;
    --deep-blue: #003f63;
    --mid-blue: #2b6a96;
    --gold: #f5b315;
    --white: #ffffff;
  }
  html, body { margin: 0; padding: 0; overflow: hidden; }
  body { width: 1200px; height: 1200px; background: var(--white); }
  .cover {
    position: relative; width: 1200px; height: 1200px; overflow: hidden;
    background: var(--deep-blue);
  }
  .cover p, .cover h1, .brand-mark { white-space: nowrap; }
  .kitchen-photo {
    position: absolute; left: 0; top: 0; width: 1200px; height: 920px;
    background: linear-gradient(180deg, #ffffff 0%, #ffffff 18%, #dfe5ea 36%, #8ea6bb 54%, #3f6d92 72%, #1c5479 88%, var(--deep-blue) 100%);
  }
  .brand-mark {
    position: absolute; left: 845px; top: 36px; width: 330px;
    font-family: "Oswald", sans-serif; font-weight: 700; color: var(--navy);
    font-size: 50px; line-height: 1.2; text-align: center; text-transform: uppercase;
  }
  .headline {
    position: absolute; left: 40px; top: 120px; margin: 0;
    font-family: "Anton", sans-serif; font-weight: 400; font-size: 250px;
    line-height: 1; letter-spacing: 6px; text-transform: uppercase;
    background: linear-gradient(180deg, #1c3a57 30%, #2f6a9a 100%);
    -webkit-background-clip: text; background-clip: text; color: transparent;
    transform: scale(0.93, 1.5); transform-origin: left top;
    -webkit-text-stroke: 1px rgba(255,255,255,0.4);
  }
  .headline-script {
    position: absolute; left: 50px; top: 330px; margin: 0;
    font-family: "Allura", cursive; font-weight: 400; font-size: 220px;
    line-height: 1; color: var(--gold);
    text-shadow: 0 3px 6px rgba(0,0,0,0.35);
  }
  .name-band {
    position: absolute; left: 0; top: 774px; width: 900px; height: 141px;
    border-top: 2px solid var(--gold); border-bottom: 2px solid var(--gold);
    background: linear-gradient(90deg, #10476d 0%, #3f7398 50%, #7596ae 100%);
  }
  .guest-name {
    position: absolute; left: 60px; top: 796px; width: 540px; margin: 0;
    text-align: center; font-family: "Allura", cursive; font-size: 92px;
    line-height: 1; color: var(--white); font-weight: 400;
  }
  .guest-title {
    position: absolute; left: 169px; top: 928px; width: 330px; margin: 0;
    text-align: center; font-family: "Poppins", sans-serif; font-size: 24px;
    letter-spacing: 1.5px; color: var(--white);
  }
  .title-rule {
    position: absolute; left: 169px; top: 968px; width: 330px; height: 2px; background: var(--gold);
  }
  .guest-company {
    position: absolute; left: 150px; top: 978px; width: 370px; margin: 0;
    text-align: center; font-family: "Poppins", sans-serif; font-size: 32px;
    letter-spacing: 2.5px; color: var(--white);
  }
  .guest-frame { position: absolute; left: 580px; top: 554px; width: 580px; height: 580px; }
</style>
</head>
<body>
  <main class="cover">
    <div class="kitchen-photo" role="img" aria-label="Blurred photo of a chef plating salads in a professional kitchen, fading into brand blue"></div>

    <div class="brand-mark">Kestrel Table<br>Hour</div>

    <h1 class="headline">Kestrel</h1>
    <p class="headline-script">Table Hour</p>

    <div class="name-band"></div>
    <p class="guest-name">Marten Ellis</p>
    <p class="guest-title">Professional Title</p>
    <div class="title-rule"></div>
    <p class="guest-company">Company Name</p>

    <svg class="guest-frame" viewBox="0 0 580 580">
      <circle cx="290" cy="290" r="290" fill="var(--gold)"/>
      <circle cx="290" cy="290" r="268" fill="var(--navy)"/>
      <circle cx="290" cy="290" r="258" fill="#e6ebf0" role="img" aria-label="Guest headshot placeholder: smiling guest in a navy sweater, arms crossed, on white"/>
    </svg>
  </main>
</body>
</html>
```